Business Card Design

We need a business card designed to the point of print ready to take to our printers. the design should be professional, easy to read and simple. The cards should represent our business as professional and trust worthy.

Attached are several versions o the logo, and also the details for the card to be printed. please do communicate if different versions of the logo is required.

Business

```html
<!DOCTYPE html>
<html lang="en">
<head>
<meta charset="utf-8">
<title>FundGather Pty Ltd – Business Card</title>
<link rel="stylesheet" href="https://fonts.googleapis.com/css2?family=Tinos:wght@400;700&display=swap">
<style>
  :root {
    --paper: #ffffff;
    --brand-grey: #5e6062;
    --accent-orange: #e9812b;
    --text-grey: #6f7072;
    --text-dark: #4a4b4d;
    --photo-tone: #f1ddd0;
  }
  * { margin: 0; padding: 0; box-sizing: border-box; }
  html, body { width: 1200px; height: 695px; overflow: hidden; background: var(--paper); }
  .card { position: relative; width: 1200px; height: 695px; background: var(--paper); overflow: hidden; }

  .banknote-photo {
    position: absolute; left: 170px; top: 55px; width: 860px; height: 505px;
    background: radial-gradient(ellipse 50% 50% at 50% 50%, var(--photo-tone) 0%, rgba(241,221,208,.6) 55%, rgba(241,221,208,0) 100%);
  }

  .company-name {
    position: absolute; left: 0; width: 1200px; top: 250px; text-align: center;
    font-family: "Tinos", "Times New Roman", serif; font-weight: 700;
    font-size: 84px; line-height: 1; color: var(--brand-grey);
  }

  .holder { position: absolute; left: 80px; top: 526px; width: 430px; text-align: center; font-family: "Tinos", "Times New Roman", serif; color: var(--accent-orange); }
  .holder-name { font-size: 54px; line-height: 1; }
  .holder-role { font-size: 42px; line-height: 1.05; margin-top: 2px; }
  .holder-rule { display: block; margin-top: 4px; }

  .contact { position: absolute; left: 621px; top: 513px; list-style: none; font-family: "Tinos", "Times New Roman", serif; font-size: 25px; line-height: 36px; color: var(--text-dark); }
  .contact .label { font-weight: 700; color: var(--text-grey); }
</style>
</head>
<body>
<main class="card">
  <div class="banknote-photo" role="img" aria-label="Photograph of fanned-out banknotes fading into white"></div>

  <h1 class="company-name">FundGather Pty Ltd</h1>

  <section class="holder">
    <p class="holder-name">Reid Maddox</p>
    <p class="holder-role">Director</p>
    <svg class="holder-rule" width="430" height="14" viewBox="0 0 430 14" aria-hidden="true">
      <defs>
        <linearGradient id="rule-grey" x1="0" x2="1">
          <stop offset="0" stop-color="#5e6062" stop-opacity="0"/>
          <stop offset="1" stop-color="#5e6062"/>
        </linearGradient>
        <linearGradient id="rule-orange" x1="0" x2="1">
          <stop offset="0" stop-color="#e9812b" stop-opacity="0"/>
          <stop offset="1" stop-color="#e9812b"/>
        </linearGradient>
      </defs>
      <rect x="0" y="3" width="430" height="2" fill="url(#rule-grey)"/>
      <rect x="0" y="8" width="430" height="3" fill="url(#rule-orange)"/>
    </svg>
  </section>

  <ul class="contact">
    <li><span class="label">phone:</span> +61 400 555 162</li>
    <li><span class="label">email:</span> rmaddox@fundgather.com.au</li>
    <li><span class="label">web:</span> www.fundgather.com.au</li>
    <li><span class="label">postal:</span> PO Box 2710 Harbour Centre Qld 4220</li>
  </ul>
</main>
</body>
</html>
```